Homepage for the brisk-trail Web Application

At the end of this text, you will find a link to a website that is under construction for a webApp that I intend to launch soon. The contest goal is for you to make redesign the homepage in a nice, fresh, modern Style. Only design, no coding necessary. It needs to have a responsive version for small screens like smart phones. Attached is the text for it, and some images that you may use. You are welcome to find or create additional supporting images. You can use PixVaultimages.com or similar service to find new images as long as I can purchase the non-exclusive use rights for the images at similar prices. The contest is just for the home page. However, the winner, if I like the work and we can agree on a fair price, could be contracted on a one-on-one basis to do the rest of the site. You are welcome to suggest minor changes like font sizes and minor variations on the Header banner, but that banner is consistent with the user interface of the application therefore should not change too much. The information should flow somewhat continually without much use of side bars or things like that.
https://www.brisk-trail-example.com
Sincerely,
Marco R. Delgado

```html
<!DOCTYPE html>
<html lang="en">
<head>
<meta charset="utf-8">
<title>Brisk-Trail — Find any document or item instantly</title>
<link rel="stylesheet" href="https://fonts.googleapis.com/css2?family=Quicksand:wght@500;600;700&family=Open+Sans:ital,wght@0,300;0,400;0,600;0,700;1,400&display=swap">
<style>
:root{
  --orange:#f9795a;
  --blue:#0a6db1;
  --blue-dark:#0762a3;
  --ink:#3d3d3d;
  --body:#555;
  --page:#f4f4f4;
  --white:#fff;
  --teal:#3ec3c9;
}
*{margin:0;padding:0;box-sizing:border-box}
html,body{width:1200px;height:3324px;overflow:hidden}
body{position:relative;background:var(--page);font-family:"Open Sans",sans-serif;color:var(--body)}
.abs{position:absolute}
.head-font{font-family:"Quicksand",sans-serif}

/* header */
.site-header{left:0;top:0;width:1200px;height:85px;background:var(--white);border-bottom:1px solid #eee}
.brand{display:flex;align-items:center;gap:8px;font-family:"Quicksand",sans-serif;font-weight:600;color:var(--orange)}
.brand-mark{border:3px solid #333;border-radius:50%}
.site-header .brand{left:142px;top:30px;font-size:26px}
.site-header .brand-mark{width:28px;height:28px}
.field{height:24px;border-radius:12px;background:#ececec;font-size:9px;color:#999;padding:6px 12px}
.login{left:1095px;top:14px;width:60px;height:24px;border-radius:12px;background:var(--orange);color:#fff;font-size:9px;font-weight:700;text-align:center;line-height:24px}
.main-nav{left:552px;top:58px;width:600px;display:flex;justify-content:space-between;font-size:10px;font-weight:700;color:#333}
.main-nav .active{color:var(--orange)}

.column{left:68px;top:85px;width:1063px;height:3060px;background:var(--white)}

/* hero */
.hero-band{left:68px;top:548px;width:1063px;height:152px;background:var(--blue)}
.hero-art{left:100px;top:140px;width:500px;height:540px;border-radius:24px;background:linear-gradient(160deg,#6fd6d9,#2aa9b3 60%,#1a7f98)}
.hero-title{left:552px;top:195px;font-size:53px;line-height:58px;font-weight:700;color:#444}
.hero-rule{left:557px;top:343px;width:73px;height:2px;background:var(--orange)}
.hero-text{left:652px;top:338px;width:395px;font-size:10.5px;line-height:18px}
.hero-tag{left:530px;top:593px;width:540px;text-align:center;color:#fff;font-size:22px;line-height:27px;font-weight:600}

.vline{width:2px;background:var(--orange)}
.section-title{width:1200px;left:0;text-align:center;font-size:44px;line-height:50px;font-weight:600;color:#444}
.section-title em{font-style:normal;color:var(--orange)}
.sub-title{width:1200px;left:0;text-align:center;font-family:"Quicksand",sans-serif;font-size:28px;font-weight:700;color:var(--blue)}
.copy{left:185px;width:830px;text-align:center;font-size:10.5px;line-height:18px}
.copy p+p{margin-top:18px}

/* items */
.item-art{width:90px;height:128px;border-radius:10px;background:linear-gradient(160deg,#8fe3e6,#35b4bd 70%,#f9795a)}
.item h3{font-family:"Quicksand",sans-serif;font-size:19px;line-height:23px;font-weight:600;color:#333}
.item .rule{width:40px;height:2px;background:var(--orange);margin:12px 0 13px}
.item p{font-size:10.5px;line-height:18px}

.alt-band{left:68px;top:2324px;width:1063px;height:286px;background:linear-gradient(135deg,var(--blue),var(--blue-dark))}
.alt-title{color:#fff;font-size:44px;font-weight:700}
.alt-text{left:230px;width:740px;text-align:center;color:#fff;font-size:10.5px;line-height:18px}

.why-title{left:152px;top:2695px;font-size:44px;font-weight:700;color:#444}
.check{display:flex;gap:14px;font-size:10.5px;line-height:18px}
.check svg{flex:none;width:20px;height:18px}

.cta-brand{left:0;width:1200px;justify-content:center;top:2942px;font-size:27px}
.cta-brand .brand-mark{width:30px;height:30px}
.cta{left:456px;top:3013px;width:288px;height:48px;border-radius:24px;background:var(--orange);color:#fff;font-family:"Quicksand",sans-serif;font-weight:700;font-size:24px;text-align:center;line-height:48px}

.site-footer{left:0;top:3145px;width:1200px;height:80px;background:var(--blue)}
.foot-nav{left:274px;top:3181px;width:654px;display:flex;justify-content:space-between;color:#fff;font-size:10px;font-weight:700}
.copyright{left:0;top:3263px;width:1200px;text-align:center;font-family:"Quicksand",sans-serif;font-size:16px;font-weight:600;color:#333}
</style>
</head>
<body>
<header class="site-header abs">
  <div class="brand abs"><span class="brand-mark"></span>Brisk Trail</div>
  <div class="field abs" style="left:709px;top:14px;width:177px">Username</div>
  <div class="field abs" style="left:897px;top:14px;width:189px">Password</div>
  <div class="login abs">LOGIN</div>
  <nav class="main-nav abs"><span class="active">HOME</span><span>PRICING</span><span>BLOG</span><span>FAQs</span><span>SUPPORT</span><span>REVIEWS</span><span>CONTACT</span><span>FREE-TRIAL</span></nav>
</header>

<div class="column abs"></div>
<svg class="abs" style="left:1131px;top:1030px" width="69" height="505" viewBox="0 0 69 505"><polygon points="0,45 69,0 69,440 0,503" fill="#0a6db1"/></svg>
<svg class="abs" style="left:0;top:2195px" width="68" height="645" viewBox="0 0 68 645"><polygon points="0,0 68,50 68,645 0,595" fill="#f9795a"/></svg>

<section>
  <div class="hero-band abs"></div>
  <div class="hero-art abs" role="img" aria-label="Isometric illustration of a laptop with filing drawers and a man holding a folder"></div>
  <h1 class="hero-title head-font abs">Find any document<br>or item instantly!</h1>
  <div class="hero-rule abs"></div>
  <p class="hero-text abs">Brisk-Trail is a system that allows you to quickly search for the location of every item that you store or file. It is an essential tool for keeping track of paper documents or any other kind of physical item. You'll have the ability to quickly find any item you're searching for, even years after you've stored it. More importantly, using Brisk-Trail helps you save considerable space without losing speedy accessibility to your treasured items.</p>
  <p class="hero-tag head-font abs">Keeping track of all your paper documents and other belongings has never been easier!</p>
</section>

<section>
  <div class="vline abs" style="left:599px;top:752px;height:53px"></div>
  <h2 class="section-title head-font abs" style="top:827px">Why use a storage management<br>system like <em>Brisk-Trail</em>?</h2>
  <h3 class="sub-title abs" style="top:987px">MANAGING PAPER DOCUMENTS</h3>
  <div class="copy abs" style="top:1032px">
    <p>Most people and businesses have a variety of documents that need to be filed. The problem is how to do it efficiently so that anything you need can easily be found, even well into the future. Normally, you'd put them in folders on file drawers, sorted in some sort of fashion. But which standard is correct for all kinds of documents? There is no set criterion for every kind of document, so you need to use a combination of them.</p>
    <p>As time passes, you might have a difficult time recalling what criterion you used to file your documents, making it hard to find that document with ease. You might not even find it at all. It becomes even more complex when the person doing the searching isn't the same one as who filed it years ago.</p>
    <p>It is estimated that workers spend over 20% of their time managing documents. A storage management system like Brisk-Trail allows any authorized user to instantly find any document regardless of who filed it or which criterion was used, as long as it was properly filed using the system.</p>
  </div>
  <h3 class="sub-title abs" style="top:1269px">MANAGING ANY NON-DOCUMENT OBJECTS</h3>
  <p class="abs" style="left:0;top:1309px;width:1200px;text-align:center;font-size:11px;font-style:italic">The same is true of storing any other kind of objects. Common examples include:</p>

  <div class="item-art abs" style="left:115px;top:1382px" role="img" aria-label="Phone with storage drawers illustration"></div>
  <div class="item abs" style="left:233px;top:1381px;width:315px"><h3>Storage boxes, closets,<br>warehouses, and shelves</h3><div class="rule"></div><p>Anything that you put away in storage, would better be indexed with a system that lets you find what you're looking for instantly. Otherwise, you are better off getting rid of those items. In addition to helping you find any object quickly and easily, proper use of Brisk-Trail could help you save lots of space!</p></div>

  <div class="item-art abs" style="left:638px;top:1380px" role="img" aria-label="Phone with drawer and books illustration"></div>
  <div class="item abs" style="left:776px;top:1380px;width:315px"><h3>Books</h3><div class="rule"></div><p>Anything that you put away in storage, would better be indexed with a system that lets you find what you're looking for instantly. Otherwise, you are better off getting rid of those items. In addition to helping you find any object quickly and easily, proper use of Brisk-Trail could help you save lots of space!</p></div>

  <div class="item-art abs" style="left:115px;top:1602px" role="img" aria-label="Phone with drawer and wine bottle illustration"></div>
  <div class="item abs" style="left:233px;top:1601px;width:315px"><h3>Wines</h3><div class="rule"></div><p>Maintaining a constant temperature is essential for good care of quality wines. If you are a wine enthusiast, and have even a small wine cellar fridge, keeping your wines indexed on our system would prove invaluable in selecting and locating a wine bottle for any moment without opening that cellar fridge door for too long.</p></div>

  <div class="item-art abs" style="left:636px;top:1588px" role="img" aria-label="Phone with storage drawers illustration"></div>
  <div class="item abs" style="left:774px;top:1587px;width:315px"><h3>Safety boxes</h3><div class="rule"></div><p>It is common for people to forget exactly which valuables they have stored in their safety boxes or bank safety deposit boxes.</p></div>

  <div class="item-art abs" style="left:636px;top:1756px" role="img" aria-label="Phone with drawer and test tube illustration"></div>
  <div class="item abs" style="left:774px;top:1752px;width:320px"><h3>Test samples</h3><div class="rule"></div><p>Laboratory samples frequently need to be stored at constant cold temperatures. Our system was originally designed to fulfill the needs of a laboratory which needs an efficient way to minimize the time that the door of their specialized freezers is open while searching for a sample. For confidentiality reasons, each vial was only identified with a code and all the details of the sample and patient would be recorded on our secure system.</p></div>

  <div class="item-art abs" style="left:115px;top:1818px" role="img" aria-label="Phone with storage drawers illustration"></div>
  <div class="item abs" style="left:233px;top:1817px;width:315px"><h3>Moving boxes</h3><div class="rule"></div><p>It is always a good idea to record in detail the contents of each box when you move. Since Brisk-Trail works well on any modern smartphone, it is easy to record each item as you pack it. After the move, the system makes it easy for you to check that everything that you packed arrived as it should. In addition, if you leave some boxes unopened for a long time, you will always be able to locate the items inside in no time.</p></div>

  <div class="item-art abs" style="left:636px;top:1998px" role="img" aria-label="Phone with drawer and key illustration"></div>
  <div class="item abs" style="left:774px;top:1995px;width:315px"><h3>Keys</h3><div class="rule"></div><p>In a situation such a property management, you can keep track of hundreds of keys for every property you manage. Using Brisk-Trail will easily organize your key boxes without losing track of where the keys for each property are located.</p></div>

  <div class="item-art abs" style="left:115px;top:2058px" role="img" aria-label="Phone with drawer and disc illustration"></div>
  <div class="item abs" style="left:233px;top:2056px;width:315px"><h3>Audio, video, data, and<br>removable media</h3><div class="rule"></div><p>Keeping track of the content and storage location of removable media can be a hassle. A system like ours can really help to make that task a breeze.</p></div>
</section>

<section>
  <div class="alt-band abs"></div>
  <div class="abs" style="left:602px;top:2282px;width:1px;height:86px;background:#9aa"></div>
  <h2 class="section-title alt-title head-font abs" style="top:2412px">Alternative uses for Brisk-Trail</h2>
  <p class="alt-text abs" style="top:2477px">How many times have you gone to a restaurant and couldn't recall how good (or bad) each of the dishes were that you previously ordered? You can use Brisk-Trail to record each one to improve your experience for every visit. Our app can also help you decide where you want to go or which dish to recommend when you have a special occasion.</p>
</section>

<section>
  <h2 class="why-title head-font abs">Why Brisk-Trail?</h2>
  <div class="check abs" style="left:152px;top:2762px;width:420px"><svg viewBox="0 0 20 18"><path d="M2 9l5 6L18 2" fill="none" stroke="#f9795a" stroke-width="2.5"/></svg><span>It is extremely easy to use.</span></div>
  <div class="check abs" style="left:152px;top:2798px;width:420px"><svg viewBox="0 0 20 18"><path d="M2 9l5 6L18 2" fill="none" stroke="#f9795a" stroke-width="2.5"/></svg><span>It Adapts to your stile. Since each catalog can have 1 or more levels of depth (folders and sub-folders), Brisk-Trail does not force you to use a specific filing or storage methodology.</span></div>
  <div class="check abs" style="left:620px;top:2762px;width:460px"><svg viewBox="0 0 20 18"><path d="M2 9l5 6L18 2" fill="none" stroke="#f9795a" stroke-width="2.5"/></svg><span>It's very affordable. Checkout our pricing plans!</span></div>
  <div class="check abs" style="left:620px;top:2798px;width:460px"><svg viewBox="0 0 20 18"><path d="M2 9l5 6L18 2" fill="none" stroke="#f9795a" stroke-width="2.5"/></svg><span>Since it is online, your data is available almost anywhere in the world.</span></div>
  <div class="check abs" style="left:620px;top:2834px;width:460px"><svg viewBox="0 0 20 18"><path d="M2 9l5 6L18 2" fill="none" stroke="#f9795a" stroke-width="2.5"/></svg><span>Data encryption ensures that your information is always private, safe, and secure.</span></div>

  <div class="brand cta-brand abs"><span class="brand-mark"></span>Brisk Trail</div>
  <div class="cta abs">30 DAY FREE TRIAL</div>
</section>

<footer>
  <div class="site-footer abs"></div>
  <nav class="foot-nav abs"><span>HOME</span><span>PRICING</span><span>BLOG</span><span>FAQs</span><span>SUPPORT</span><span>REVIEWS</span><span>CONTACT</span><span>FREE-TRIAL</span></nav>
  <p class="copyright abs">©2021. Brisk-Trail. All Rights Reserved</p>
</footer>
</body>
</html>
```